Verpackungsdesign einer Faltschachtel für Haarteile & Perücken
Zielgruppe
Wir Produzieren Haarteile und Perücken
www.lunavell.de
Aufgabenstellung
Einen KartonF Faltschachtel in Schuhkartongröße. 20cm 16 cm 12 cm
Unser logo und der text soll auf der schachtel untergebracht werden.
https://www.faltwerkpost.de/krempelverpackung-drucken.html
matte folie
innen und außen druck
Der Karton sollte möglich dunkle farben haben. kann auch gerne fast schwarz sein.
Krempelschachtel - 380g/m² Norda Board - 20 cm x 16 cm x 12 cm - 2000 Stück - 12 Werktage Produktionszeit - 4-farbig bedruckt - Matte Folie - Ohne Heißfolie - Ohne Fenster - 4/4 farbig (aussen+innen)

```html
<!DOCTYPE html>
<html lang="de">
<head>
<meta charset="utf-8">
<title>Lunavell – Faltschachtel</title>
<link href="https://fonts.googleapis.com/css2?family=Open+Sans:wdth,wght@75..100,300..800&display=swap" rel="stylesheet">
<style>
:root{
  --ink:#000;
  --paper:#fff;
  --field:#f2ebe2;
  --text:#2b2b2b;
  --muted:#555;
  --gold:#d8c29a;
  --guide:#d3141b;
}
*{margin:0;padding:0;box-sizing:border-box}
html,body{width:697px;height:1200px;overflow:hidden;background:var(--paper)}
body{position:relative;font-family:"Open Sans",Arial,sans-serif;font-stretch:75%;color:var(--text)}
.dieline{position:absolute;left:0;top:0}
.brand{position:absolute;display:flex;align-items:center;gap:.25em;color:var(--gold);font-weight:400;letter-spacing:.01em;white-space:nowrap;transform:translate(-50%,-50%);line-height:1}
.brand__dot{width:1.05em;height:1.05em;border:1px solid var(--gold);border-radius:50%}
.is-mini{position:absolute;transform-origin:0 0;transform:scale(.597)}

/* customer form */
.form-card{width:241px;height:167px;background:var(--paper);border-radius:3px;position:relative}
.form-card .lbl{position:absolute;font-weight:700;font-size:6.6px;line-height:1;color:#111}
.form-card .lbl small{display:block;font-size:3.6px;line-height:1.1}
.form-card .field{position:absolute;background:var(--field);height:11px}
.consult{position:absolute;left:8px;top:52px;font-size:4.3px;color:var(--muted)}
.opt{position:absolute;font-size:4.3px;color:var(--muted);display:flex;align-items:center;gap:2px;white-space:nowrap}
.box{display:inline-block;width:4px;height:4px;background:var(--field)}
.log-head{position:absolute;top:77px;font-weight:700;font-size:4.7px;color:#111}
.log-rows{position:absolute;left:8px;top:83px;width:226px;display:grid;grid-template-columns:44px 149px 29px;column-gap:2px;row-gap:1.8px}
.log-rows span{height:11.5px;background:var(--field)}

/* care sheet */
.care-sheet{width:268px;height:210px;position:relative}
.care-card{position:absolute;left:0;width:268px;background:var(--paper);border-radius:2px;padding:5px 7px 0}
.care-card h3{font-size:5.2px;font-weight:700;color:#111;line-height:1.3;margin-bottom:.6px}
.care-card p{font-size:3.95px;line-height:6.1px;color:var(--muted);text-align:justify}
.care-card--care{top:0;height:69px}
.care-card--effects{top:77px;height:71px}
.care-card--quality{top:157px;height:53px}
.care-card .note{text-align:left;width:138px}
.contact{position:absolute;left:149px;top:46px;width:121px;height:24px;background:var(--ink);border-radius:4px 0 0 0;padding:3px 0 0 6px}
.contact__head{font-size:4.6px;font-weight:700;color:var(--gold);letter-spacing:.02em}
.contact__body{display:flex;align-items:center;gap:4px;margin-top:1.5px;color:var(--paper);font-weight:700;font-size:4.6px;line-height:5.4px}
.contact__dot{width:11px;height:11px;border:.7px solid var(--paper);border-radius:50%}
.contact__sep{width:.6px;height:10px;background:var(--paper)}
.q-col{position:absolute;font-size:3.7px;color:var(--muted);line-height:6.2px}
.q-col div{display:flex;align-items:center;gap:2px;white-space:nowrap}
.q-col .box{width:3.6px;height:3.6px}
.q-sub{position:absolute;font-weight:700;font-size:4.8px;color:#111}
.scale{position:absolute;top:47px;font-size:3.6px;color:var(--muted);display:flex;align-items:center;gap:2px;white-space:nowrap}
.scale b{color:#111}
.badge{position:absolute;left:241px;top:187px;width:30px;height:30px;border-radius:50%;background:var(--ink);border:1.2px solid #ddd;box-shadow:0 0 0 3px var(--ink)}

/* presentation panels */
.panel{position:absolute;background:var(--ink);box-shadow:0 4px 10px rgba(0,0,0,.35)}
.panel--care{left:57px;top:639px;width:333px;height:242px}
.panel--form{left:294px;top:912px;width:334px;height:240px}
.panel svg{position:absolute;left:0;top:0}
</style>
</head>
<body>

<svg class="dieline" width="697" height="640" viewBox="0 0 697 640" aria-hidden="true">
  <path fill="#000" d="M262,28 H436 C480,28 517,70 517,104 L427,129 L436,133 C480,137 503,170 503,200 V245 L421,269 H497 V373 H656 V504 H497 V604 Q497,608 493,608 H436 L434,610 H264 L262,608 H205 Q199,608 199,604 V504 H41 V373 H199 V269 H276 L194,245 V200 C194,170 217,137 261,133 L270,129 L180,104 C180,70 217,28 262,28 Z"/>
</svg>

<div class="brand" style="left:348px;top:144px;font-size:11px"><span class="brand__dot"></span>lunavell</div>

<div class="is-mini" style="left:276px;top:156px">
  <div class="form-card">
    <div class="lbl" style="left:8px;top:8px">KUNDENNAME</div>
    <div class="field" style="left:52px;top:7px;width:57px"></div>
    <div class="lbl" style="left:115px;top:8px">TELEFONNUMMER</div>
    <div class="field" style="left:171px;top:7px;width:63px"></div>
    <div class="lbl" style="left:8px;top:23px">FÄRBUNG<small>(EIGENHAAR)</small></div>
    <div class="field" style="left:38px;top:23px;width:71px"></div>
    <div class="lbl" style="left:115px;top:23px">FÄRBUNG<small>(FREMDHAAR)</small></div>
    <div class="field" style="left:147px;top:23px;width:87px"></div>
    <div class="consult">Beratung für</div>
    <div class="opt" style="left:31px;top:52px"><span class="box"></span>Orla Haarverdichtung</div>
    <div class="opt" style="left:95px;top:52px"><span class="box"></span>Graft Haarsysteme</div>
    <div class="opt" style="left:145px;top:52px"><span class="box"></span>Maßanfertigung</div>
    <div class="opt" style="left:31px;top:59px"><span class="box"></span>Orlaweave Haarverlängerung</div>
    <div class="opt" style="left:95px;top:59px"><span class="box"></span>Haarsyteme, Perücken</div>
    <div class="log-head" style="left:8px">DATUM</div>
    <div class="log-head" style="left:55px">DIENSTLEISTUNG / PRODUKTVERKAUF</div>
    <div class="log-head" style="left:205px">PREIS</div>
    <div class="log-rows">
      <span></span><span></span><span></span><span></span><span></span><span></span>
      <span></span><span></span><span></span><span></span><span></span><span></span>
      <span></span><span></span><span></span><span></span><span></span><span></span>
    </div>
  </div>
</div>

<div class="is-mini" style="left:269px;top:375px">
  <div class="care-sheet">
    <div class="care-card care-card--care">
      <h3>Besondere Pflege</h3>
      <p>Der Kunde verpflichtet sich zur sachgemäßen Handhabung und Pflege des Produktes bzw. der Haare. Dazu gehört das genaue beachten der Pflegeanweisung (der Lunavell GmbH). Wichtige Punkte sind die Verwendung der empfohlenen Pflegeprodukte(der Lunavell GmbH) oder absolut gleichwertige Pflegeprodukte. Und die Einhaltung der Benutzungsregelung. Wir empfehlen die Haarverlängerung oder das Haarsystem maximal einmal in der Woche zu reinigen und Haare niemals direkt oder mit kreisenden Bewegungen zu shampoonieren. Außerdem muss nach jeder Berührung mit Wasser ausreichend Pflegespülung (der Lunavell GmbH) in das Haar eingekämmt werden. Beachten Sie hierzu die genau Pflegeanweisung. Kein übermäßiges aber vorsichtiges und regelmäßiges Bürsten der Haare und sofortiges auskämmen von Verknotungen oder Verfilzungen. Haare beim Schlaf oder bei starker Aktivität zusammenbinden, den Ansatz der Haare immer vollständig trocknen. Bei falscher Pflege kann das Eigenhaar und das Haarsystem signifikant verknoten.</p>
      <p class="note" style="margin-top:2px">Haarsysteme wirken am Scheitel und Wirbel immer leichter, das berechtigt nicht zu Reklamation.</p>
      <p class="note" style="margin-top:2px">Lagernde Haarsysteme gelten als neu, unabhängig Ihrer Lagerdauer.</p>
      <div class="contact">
        <div class="contact__head">HABEN SIE FRAGEN? WIR HELFEN IHNEN GERNE WEITER.</div>
        <div class="contact__body"><span class="contact__dot"></span><div>+49 (0) 761/4820150-0<br>+49 (0) 152/40718265</div><span class="contact__sep"></span><div>s@lunavell.de<br>www.lunavell.de</div></div>
      </div>
    </div>
    <div class="care-card care-card--effects">
      <h3>Nebenwirkungen</h3>
      <p>Haarverlängerungen und Haarsysteme aus echten Haaren haben bei sachgemäßer Pflege und Handhabung in der Regel nur wenig Einfluss oder Nebenwirkungen auf den menschlichen Körper. Dennoch ist es möglich, dass die Haarverlängerung oder das Haarsystem auf bestimmte Weise auf den Körper wirken, insbesondere wenn eine Haarverlängerung oder Haarsystem dauerhaft am Körper befestigt ist. Daher ist die Befestigung kein ausdrücklicher Vertragsbestandteil. Folgende Nebenwirkungen können bei einem Haarsystem oder einer Haarverlängerung am Körper auftreten: Wahrnehmen und spüren der Haare sind normale Begleiterscheinungen, es ist möglich, dass das Haarsystem oder die Haarverlängerung insbesondere in den ersten Tagen oder Wochen besonders stark wahrgenommen wird. Und kann insbesondere in den ersten Tagen der Befestigung auch zu Kopfschmerzen führen. Eine dauerhafte Befestigung des Haarsystems oder der Haarverlängerung kann zu Hautentzündungen oder Schuppen auf der Haut führen. Dies ist selten der Fall und kann in der Regel durch besondere Pflege der Kopfhaut reguliert werden. Falls nicht wird ein Wechsel der Befestigung empfohlen und das Tragen der Haare ist auf wenige Stunden pro Tag zu reduzieren. Ausbleichen der Haare über den Tragezeitraum und der Verschleiß der Haare in Form von stumpfer werdendem Haar und Spliss in den Spitzen sind normale Begleiterscheinung. Auch leichter Haarverlust am Produkt und leichter Eigenhaarverlust. Bei besonderen, gesundheitlichen Einschränkungen des Kunden, verpflichtet sich dieser die seinen Dienstleister schriftlich darüber zu informieren.</p>
    </div>
    <div class="care-card care-card--quality">
      <h3>Um welche Haarqualität handelt es sich</h3>
      <div class="q-col" style="left:7px;top:10px">
        <div><span class="box"></span>Kunsthaar &nbsp;Graues Haar: <span class="box"></span>Kunsthaar <span class="box"></span>Yak <span class="box"></span>Echt blond. <span class="box"></span>Mischung Exp.</div>
        <div><span class="box"></span>Indisches Echthaar veredelt (chemisch blondiert, oxidativ gefärbt, chemisch entschuppt)</div>
        <div><span class="box"></span>Indisches Echthaar remy ver. (chemisch blondiert, oxidativ gefärbt, teil chemisch entschuppt)</div>
        <div><span class="box"></span>Europäisches Echthaar (chemisch blondiert, oxidativ gefärbt, chemisch entschuppt)</div>
      </div>
      <div class="q-col" style="left:135px;top:4px">
        <div><span class="box"></span>Schnitthaar (nicht Europäisch) (chemisch blondiert, oxidativ gefärbt, teil chemisch entschuppt)</div>
        <div><span class="box"></span>Schnitthaar (nicht Europäisch) (chemisch blondiert, teil chemisch entschuppt)</div>
        <div><span class="box"></span>Schnitthaar Europäisch (chemisch blondiert, oxidativ gefärbt, teil chemisch entschuppt)</div>
        <div><span class="box"></span>Schnitthaar Europäisch (chemisch blondiert, teil chemisch entschuppt)</div>
        <div><span class="box"></span>Schnitthaar Europäisch Unbehandelt, teil chemisch entschuppt</div>
      </div>
      <div class="q-sub" style="left:7px;top:39px">Grad der Blondierung</div>
      <div class="scale" style="left:7px"><b>sehr wenig</b>(gut) <span class="box"></span><span class="box"></span><span class="box"></span><span class="box"></span><span class="box"></span><span class="box"></span><span class="box"></span> <b>sehr stark</b>(starke Strukturschwächung)</div>
      <div class="q-sub" style="left:135px;top:44px">Dauerwelle</div>
      <div class="scale" style="left:163px"><span class="box"></span><b>ja</b>&nbsp;&nbsp;&nbsp;&nbsp;&nbsp;<span class="box"></span><b>nein</b></div>
    </div>
    <div class="badge"></div>
  </div>
</div>

<section class="panel panel--care" aria-label="Innenseite Boden">
  <svg width="333" height="242" aria-hidden="true"><rect x="28" y="7" width="286" height="228" fill="none" stroke="var(--guide)" stroke-width=".6"/></svg>
</section>
<div class="is-mini" style="left:94px;top:654px;transform:none">
  <div class="care-sheet">
    <div class="care-card care-card--care">
      <h3>Besondere Pflege</h3>
      <p>Der Kunde verpflichtet sich zur sachgemäßen Handhabung und Pflege des Produktes bzw. der Haare. Dazu gehört das genaue beachten der Pflegeanweisung (der Lunavell GmbH). Wichtige Punkte sind die Verwendung der empfohlenen Pflegeprodukte(der Lunavell GmbH) oder absolut gleichwertige Pflegeprodukte. Und die Einhaltung der Benutzungsregelung. Wir empfehlen die Haarverlängerung oder das Haarsystem maximal einmal in der Woche zu reinigen und Haare niemals direkt oder mit kreisenden Bewegungen zu shampoonieren. Außerdem muss nach jeder Berührung mit Wasser ausreichend Pflegespülung (der Lunavell GmbH) in das Haar eingekämmt werden. Beachten Sie hierzu die genau Pflegeanweisung. Kein übermäßiges aber vorsichtiges und regelmäßiges Bürsten der Haare und sofortiges auskämmen von Verknotungen oder Verfilzungen. Haare beim Schlaf oder bei starker Aktivität zusammenbinden, den Ansatz der Haare immer vollständig trocknen. Bei falscher Pflege kann das Eigenhaar und das Haarsystem signifikant verknoten.</p>
      <p class="note" style="margin-top:2px">Haarsysteme wirken am Scheitel und Wirbel immer leichter, das berechtigt nicht zu Reklamation.</p>
      <p class="note" style="margin-top:2px">Lagernde Haarsysteme gelten als neu, unabhängig Ihrer Lagerdauer.</p>
      <div class="contact">
        <div class="contact__head">HABEN SIE FRAGEN? WIR HELFEN IHNEN GERNE WEITER.</div>
        <div class="contact__body"><span class="contact__dot"></span><div>+49 (0) 761/4820150-0<br>+49 (0) 152/40718265</div><span class="contact__sep"></span><div>s@lunavell.de<br>www.lunavell.de</div></div>
      </div>
    </div>
    <div class="care-card care-card--effects">
      <h3>Nebenwirkungen</h3>
      <p>Haarverlängerungen und Haarsysteme aus echten Haaren haben bei sachgemäßer Pflege und Handhabung in der Regel nur wenig Einfluss oder Nebenwirkungen auf den menschlichen Körper. Dennoch ist es möglich, dass die Haarverlängerung oder das Haarsystem auf bestimmte Weise auf den Körper wirken, insbesondere wenn eine Haarverlängerung oder Haarsystem dauerhaft am Körper befestigt ist. Daher ist die Befestigung kein ausdrücklicher Vertragsbestandteil. Folgende Nebenwirkungen können bei einem Haarsystem oder einer Haarverlängerung am Körper auftreten: Wahrnehmen und spüren der Haare sind normale Begleiterscheinungen, es ist möglich, dass das Haarsystem oder die Haarverlängerung insbesondere in den ersten Tagen oder Wochen besonders stark wahrgenommen wird. Und kann insbesondere in den ersten Tagen der Befestigung auch zu Kopfschmerzen führen. Eine dauerhafte Befestigung des Haarsystems oder der Haarverlängerung kann zu Hautentzündungen oder Schuppen auf der Haut führen. Dies ist selten der Fall und kann in der Regel durch besondere Pflege der Kopfhaut reguliert werden. Falls nicht wird ein Wechsel der Befestigung empfohlen und das Tragen der Haare ist auf wenige Stunden pro Tag zu reduzieren. Ausbleichen der Haare über den Tragezeitraum und der Verschleiß der Haare in Form von stumpfer werdendem Haar und Spliss in den Spitzen sind normale Begleiterscheinung. Auch leichter Haarverlust am Produkt und leichter Eigenhaarverlust. Bei besonderen, gesundheitlichen Einschränkungen des Kunden, verpflichtet sich dieser die seinen Dienstleister schriftlich darüber zu informieren.</p>
    </div>
    <div class="care-card care-card--quality">
      <h3>Um welche Haarqualität handelt es sich</h3>
      <div class="q-col" style="left:7px;top:10px">
        <div><span class="box"></span>Kunsthaar &nbsp;Graues Haar: <span class="box"></span>Kunsthaar <span class="box"></span>Yak <span class="box"></span>Echt blond. <span class="box"></span>Mischung Exp.</div>
        <div><span class="box"></span>Indisches Echthaar veredelt (chemisch blondiert, oxidativ gefärbt, chemisch entschuppt)</div>
        <div><span class="box"></span>Indisches Echthaar remy ver. (chemisch blondiert, oxidativ gefärbt, teil chemisch entschuppt)</div>
        <div><span class="box"></span>Europäisches Echthaar (chemisch blondiert, oxidativ gefärbt, chemisch entschuppt)</div>
      </div>
      <div class="q-col" style="left:135px;top:4px">
        <div><span class="box"></span>Schnitthaar (nicht Europäisch) (chemisch blondiert, oxidativ gefärbt, teil chemisch entschuppt)</div>
        <div><span class="box"></span>Schnitthaar (nicht Europäisch) (chemisch blondiert, teil chemisch entschuppt)</div>
        <div><span class="box"></span>Schnitthaar Europäisch (chemisch blondiert, oxidativ gefärbt, teil chemisch entschuppt)</div>
        <div><span class="box"></span>Schnitthaar Europäisch (chemisch blondiert, teil chemisch entschuppt)</div>
        <div><span class="box"></span>Schnitthaar Europäisch Unbehandelt, teil chemisch entschuppt</div>
      </div>
      <div class="q-sub" style="left:7px;top:39px">Grad der Blondierung</div>
      <div class="scale" style="left:7px"><b>sehr wenig</b>(gut) <span class="box"></span><span class="box"></span><span class="box"></span><span class="box"></span><span class="box"></span><span class="box"></span><span class="box"></span> <b>sehr stark</b>(starke Strukturschwächung)</div>
      <div class="q-sub" style="left:135px;top:44px">Dauerwelle</div>
      <div class="scale" style="left:163px"><span class="box"></span><b>ja</b>&nbsp;&nbsp;&nbsp;&nbsp;&nbsp;<span class="box"></span><b>nein</b></div>
    </div>
    <div class="badge"></div>
  </div>
</div>

<section class="panel panel--form" aria-label="Innenseite Deckel">
  <svg width="334" height="240" aria-hidden="true">
    <path d="M0,1 L30,6 L0,12 Z M334,1 L304,6 L334,12 Z M0,228 L30,234 L0,239 Z M334,228 L304,234 L334,239 Z" fill="#fff"/>
    <rect x="30" y="7" width="282" height="230" fill="none" stroke="var(--guide)" stroke-width=".6"/>
  </svg>
  <div class="brand" style="left:170px;top:30px;font-size:19px"><span class="brand__dot"></span>lunavell</div>
  <div class="form-card" style="position:absolute;left:50px;top:49px">
    <div class="lbl" style="left:8px;top:8px">KUNDENNAME</div>
    <div class="field" style="left:52px;top:7px;width:57px"></div>
    <div class="lbl" style="left:115px;top:8px">TELEFONNUMMER</div>
    <div class="field" style="left:171px;top:7px;width:63px"></div>
    <div class="lbl" style="left:8px;top:23px">FÄRBUNG<small>(EIGENHAAR)</small></div>
    <div class="field" style="left:38px;top:23px;width:71px"></div>
    <div class="lbl" style="left:115px;top:23px">FÄRBUNG<small>(FREMDHAAR)</small></div>
    <div class="field" style="left:147px;top:23px;width:87px"></div>
    <div class="consult">Beratung für</div>
    <div class="opt" style="left:31px;top:52px"><span class="box"></span>Orla Haarverdichtung</div>
    <div class="opt" style="left:95px;top:52px"><span class="box"></span>Graft Haarsysteme</div>
    <div class="opt" style="left:145px;top:52px"><span class="box"></span>Maßanfertigung</div>
    <div class="opt" style="left:31px;top:59px"><span class="box"></span>Orlaweave Haarverlängerung</div>
    <div class="opt" style="left:95px;top:59px"><span class="box"></span>Haarsyteme, Perücken</div>
    <div class="log-head" style="left:8px">DATUM</div>
    <div class="log-head" style="left:55px">DIENSTLEISTUNG / PRODUKTVERKAUF</div>
    <div class="log-head" style="left:205px">PREIS</div>
    <div class="log-rows">
      <span></span><span></span><span></span><span></span><span></span><span></span>
      <span></span><span></span><span></span><span></span><span></span><span></span>
      <span></span><span></span><span></span><span></span><span></span><span></span>
    </div>
  </div>
</section>

</body>
</html>
```